I need a business Card Design for my practice , i am clinical herbalist. I am a herbalist specializing in Lyme disease, autism, autoimmune diseases, difficult to cure diseasesDifficult to cure diseases. In my innovative practice i link traditional medicine, herbs with science, immunologu ,pharmacology.

Industry/Entity Type

Business

Contact Information for Business Card

My company name : OŚRODEK ZIELNIK
My name : Piotr Kaleta
Name of my profession : Fitoterapeuta
In Polish language Fitoterapeuta is Herbalist .

e-mail: piotrkaleta@osrodekzielnik.com
www.osrodek-zielnik.pl
phone : 604 587 231
My company adress : Dąbrowa Sitnicka 41 , 38-415 Kłodnica
I dont have logo .

Requirements
Nice to have
• My company

```html
<!DOCTYPE html>
<html lang="pl">
<head>
<meta charset="utf-8">
<title>Piotr Kaleta – Business Card</title>
<link href="https://fonts.googleapis.com/css2?family=Montserrat:wght@400;500&display=swap" rel="stylesheet">
<style>
  :root {
    --backdrop: #acacac;
    --card: #ffffff;
    --brand-green: #1b8a3c;
    --leaf-deep: #7cc43a;
    --leaf-light: #c6e25a;
    --leaf-yellow: #e3e64a;
    --sky: #f6f8fa;
  }
  * { margin: 0; padding: 0; box-sizing: border-box; }
  html, body {
    width: 1200px;
    height: 1200px;
    overflow: hidden;
    background: var(--backdrop);
  }
  .stage {
    position: relative;
    width: 1200px;
    height: 1200px;
  }
  .business-card {
    position: absolute;
    left: 61px;
    top: 286px;
    width: 1079px;
    height: 628px;
    background: var(--card);
    overflow: hidden;
    font-family: "Montserrat", sans-serif;
    color: var(--brand-green);
  }
  .foliage-photo {
    position: absolute;
    inset: 0;
    width: 860px;
    background:
      radial-gradient(ellipse 60% 75% at 30% 55%, var(--leaf-deep) 0%, var(--leaf-light) 55%, rgba(198,226,90,0) 80%),
      linear-gradient(90deg, var(--leaf-yellow) 0%, var(--leaf-deep) 30%, var(--leaf-light) 55%, var(--sky) 85%, rgba(246,248,250,0) 100%);
  }
  .card-text {
    position: absolute;
    left: 648px;
    top: 0;
    white-space: nowrap;
  }
  .person-name {
    position: absolute;
    top: 78px;
    font-size: 51px;
    font-weight: 500;
    letter-spacing: 0.5px;
  }
  .profession {
    position: absolute;
    top: 146px;
    font-size: 18px;
    font-weight: 500;
  }
  .company-name {
    position: absolute;
    top: 206px;
    font-size: 30px;
    font-weight: 400;
  }
  .contact-line {
    position: absolute;
    font-size: 18px;
    font-weight: 500;
  }
  .address { top: 248px; }
  .phone { top: 276px; }
  .email { top: 302px; }
  .website {
    position: absolute;
    top: 352px;
    font-size: 23px;
    font-weight: 500;
  }
</style>
</head>
<body>
<div class="stage">
  <div class="business-card">
    <div class="foliage-photo" role="img" aria-label="Photograph of green and yellow tree foliage with branches against a bright sky"></div>
    <div class="card-text">
      <div class="person-name">Piotr Kaleta</div>
      <div class="profession">Fitoterapeuta (Herbalist)</div>
      <div class="company-name">OŚRODEK ZIELNIK</div>
      <div class="contact-line address">Dąbrowa Sitnicka 41 , 38-415 Kłodnica</div>
      <div class="contact-line phone">Phone : 604-587-231</div>
      <div class="contact-line email">email : piotrkaleta@osrodekzielnik.com</div>
      <div class="website">www.osrodek-zielnik.pl</div>
    </div>
  </div>
</div>
</body>
</html>
```